Consultants Need a Powerful New Image to Support a New Concept

We need a better image for an idea we have. Will be used in powerpoint but also in print (workbooks, handouts etc). The notion is that in any moment people in an organisation can choose to tell positive stories about what is going well, what they enjoy, what they are hopeful for or negative stories about what is wrong, not working or they are frustrated and pissed off about.

Target Market(s)

Leaders in organisations

Industry/Entity Type

It Support

Font styles to use
Sans Serif

Requirements
Must have
• The ability to build the image in powerpoint (at least add the text). Needs also to be used as a stand alone. Font and palette consistency with other materials. Some examples attached as well as font files and colour guidelines. Notice the left hand side of the model is about tell the stories and the right hand side is about how telling positive stories encourages others to seek more positive stories. On the right hand side down the bottom, the point is that these negative stories are so easy to join in on and they spread quickly and breed cynicism. Note the "Storyline" running up and down the middle - storyline model attached.
Nice to have
• A sense of momentum both up and down - the more positive stories we tell the more the organisation is energised and positive, the more negative stories (whingeing and complaining) the worse it is.

```html
<!DOCTYPE html>
<html lang="en">
<head>
<meta charset="utf-8">
<title>The Conversational Moment</title>
<link href="https://fonts.googleapis.com/css2?family=Montserrat:wght@400;500;700&display=swap" rel="stylesheet">
<style>
  :root {
    --bg-centre: #f7f7f7;
    --bg-edge: #d6d6d6;
    --ink: #2a2a2a;
    --label: #3a3a3a;
    --blue-text: #1f5fae;
    --red-text: #c61f30;
    --teal-light: #34c3ec;
    --teal-dark: #1282b2;
    --teal-fold: #0c5f85;
    --red-light: #e2344a;
    --red-dark: #b3192b;
    --red-fold: #7d0f1c;
  }
  * { margin: 0; padding: 0; box-sizing: border-box; }
  html, body { width: 1200px; height: 849px; overflow: hidden; }
  body {
    position: relative;
    font-family: "Montserrat", sans-serif;
    background: radial-gradient(ellipse at 50% 50%, var(--bg-centre) 0%, #ececec 50%, var(--bg-edge) 100%);
  }
  .storyline { position: absolute; left: 0; top: 0; }
  .label {
    position: absolute;
    transform: translateY(-50%);
    white-space: nowrap;
    font-size: 16px;
    font-weight: 400;
    letter-spacing: 0.04em;
    color: var(--label);
  }
  .label.left { text-align: right; }
  .kicker {
    position: absolute;
    transform: translateY(-50%);
    white-space: nowrap;
    font-size: 16px;
    font-weight: 700;
    letter-spacing: 0.03em;
  }
  .headline {
    position: absolute;
    transform: translateY(-50%);
    white-space: nowrap;
    font-size: 26px;
    font-weight: 700;
  }
  .positive { color: var(--blue-text); }
  .negative { color: var(--red-text); }
  .moment {
    position: absolute;
    left: 0; width: 1200px; top: 430px;
    transform: translateY(-50%);
    text-align: center;
    font-size: 33px;
    font-weight: 400;
    letter-spacing: 0.05em;
    color: var(--ink);
  }
  .step-word {
    font-family: "Montserrat", sans-serif;
    font-weight: 700;
    font-size: 16px;
    fill: #ffffff;
    text-anchor: middle;
    dominant-baseline: middle;
  }
</style>
</head>
<body>

<svg class="storyline" width="1200" height="849" viewBox="0 0 1200 849" aria-hidden="true">
  <defs>
    <linearGradient id="teal" x1="0" x2="1" y1="0" y2="0">
      <stop offset="0" stop-color="var(--teal-dark)"/>
      <stop offset="0.45" stop-color="var(--teal-light)"/>
      <stop offset="1" stop-color="var(--teal-dark)"/>
    </linearGradient>
    <linearGradient id="crimson" x1="0" x2="1" y1="0" y2="0">
      <stop offset="0" stop-color="var(--red-dark)"/>
      <stop offset="0.45" stop-color="var(--red-light)"/>
      <stop offset="1" stop-color="var(--red-dark)"/>
    </linearGradient>
    <linearGradient id="shelf" x1="0" x2="1" y1="0" y2="0">
      <stop offset="0" stop-color="#000" stop-opacity="0"/>
      <stop offset="0.5" stop-color="#000" stop-opacity="0.18"/>
      <stop offset="1" stop-color="#000" stop-opacity="0"/>
    </linearGradient>
    <linearGradient id="band" x1="0" x2="1" y1="0" y2="0">
      <stop offset="0" stop-color="#fff" stop-opacity="0"/>
      <stop offset="0.2" stop-color="#fff" stop-opacity="0.9"/>
      <stop offset="0.8" stop-color="#fff" stop-opacity="0.9"/>
      <stop offset="1" stop-color="#fff" stop-opacity="0"/>
    </linearGradient>
  </defs>

  <g class="shelves">
    <rect x="380" y="160" width="420" height="2" fill="url(#shelf)"/>
    <rect x="330" y="214" width="500" height="2" fill="url(#shelf)"/>
    <rect x="300" y="268" width="500" height="2" fill="url(#shelf)"/>
    <rect x="270" y="322" width="520" height="2" fill="url(#shelf)"/>
    <rect x="120" y="378" width="960" height="2" fill="url(#shelf)"/>
    <rect x="120" y="480" width="960" height="2" fill="url(#shelf)"/>
    <rect x="300" y="534" width="520" height="2" fill="url(#shelf)"/>
    <rect x="320" y="588" width="500" height="2" fill="url(#shelf)"/>
    <rect x="320" y="642" width="480" height="2" fill="url(#shelf)"/>
    <rect x="380" y="696" width="420" height="2" fill="url(#shelf)"/>
  </g>
  <rect class="moment-band" x="180" y="380" width="840" height="100" fill="url(#band)"/>

  <g class="rise">
    <polygon points="630,52 680,102 661,102 661,170 602,170 602,102 581,102" fill="url(#teal)"/>
    <g class="step">
      <rect x="578" y="146" width="72" height="70" fill="url(#teal)"/>
      <rect x="578" y="146" width="72" height="9" rx="4.5" fill="var(--teal-fold)" opacity="0.55"/>
      <text class="step-word" x="608" y="176">GET</text>
    </g>
    <g class="step">
      <rect x="553" y="200" width="71" height="72" fill="url(#teal)"/>
      <rect x="553" y="200" width="71" height="9" rx="4.5" fill="var(--teal-fold)" opacity="0.55"/>
      <text class="step-word" x="584" y="229">DO</text>
    </g>
    <g class="step">
      <rect x="526" y="254" width="72" height="70" fill="url(#teal)"/>
      <rect x="526" y="254" width="72" height="9" rx="4.5" fill="var(--teal-fold)" opacity="0.55"/>
      <text class="step-word" x="557" y="282">BE</text>
    </g>
    <g class="step">
      <rect x="500" y="306" width="74" height="72" fill="url(#teal)"/>
      <rect x="500" y="306" width="74" height="9" rx="4.5" fill="var(--teal-fold)" opacity="0.55"/>
      <text class="step-word" x="532" y="336">SEE</text>
    </g>
  </g>

  <g class="fall">
    <polygon points="524,694 584,694 584,756 606,756 555,806 506,756 524,756" fill="url(#crimson)"/>
    <g class="step">
      <rect x="549" y="640" width="61" height="72" fill="url(#crimson)"/>
      <rect x="549" y="703" width="61" height="9" rx="4.5" fill="var(--red-fold)" opacity="0.55"/>
      <text class="step-word" x="579" y="694">GET</text>
    </g>
    <g class="step">
      <rect x="574" y="588" width="60" height="72" fill="url(#crimson)"/>
      <rect x="574" y="651" width="60" height="9" rx="4.5" fill="var(--red-fold)" opacity="0.55"/>
      <text class="step-word" x="602" y="639">DO</text>
    </g>
    <g class="step">
      <rect x="600" y="534" width="60" height="72" fill="url(#crimson)"/>
      <rect x="600" y="597" width="60" height="9" rx="4.5" fill="var(--red-fold)" opacity="0.55"/>
      <text class="step-word" x="628" y="584">BE</text>
    </g>
    <g class="step">
      <rect x="626" y="480" width="60" height="72" fill="url(#crimson)"/>
      <rect x="626" y="543" width="60" height="9" rx="4.5" fill="var(--red-fold)" opacity="0.55"/>
      <text class="step-word" x="655" y="522">SEE</text>
    </g>
  </g>
</svg>

<div class="label left" style="right:646px; top:138px;">ENCOURAGES</div>
<div class="label left" style="right:675px; top:189px;">PROACTIVE BEHAVIOUR</div>
<div class="label left" style="right:708px; top:240px;">GIVES INSIGHT</div>
<div class="label left" style="right:740px; top:291px;">SHAPES BELIEFS</div>
<div class="label" style="left:708px; top:187px;">SUPPORTS PERFORMANCE</div>
<div class="label" style="left:682px; top:238px;">BUILDS CONFIDENCE</div>
<div class="label" style="left:657px; top:290px;">CHANGES AWARENESS</div>

<div class="kicker positive" style="right:766px; top:339px;">TELL STORIES:</div>
<div class="headline positive" style="right:766px; top:367px;">Bright Spots &amp; Possibility</div>
<div class="kicker positive" style="left:619px; top:341px;">SEEK STORIES:</div>
<div class="headline positive" style="left:620px; top:369px;">Catch People Doing Things Right</div>

<div class="moment">THE CONVERSATIONAL MOMENT</div>

<div class="kicker negative" style="left:302px; top:490px;">TELL STORIES:</div>
<div class="headline negative" style="left:303px; top:519px;">Complaint &amp; Failure</div>
<div class="kicker negative" style="left:735px; top:490px;">JOIN STORIES:</div>
<div class="headline negative" style="left:735px; top:519px;">Cynicism, Sarcasm &amp; Negativity</div>

<div class="label left" style="right:677px; top:572px;">FUELS UNHELPFUL BELIEFS</div>
<div class="label left" style="right:713px; top:623px;">DESTROYS CONFIDENCE</div>
<div class="label left" style="right:734px; top:674px;">UNDERMINES PERFORMANCE</div>
<div class="label" style="left:722px; top:577px;">SUPPORTS PERFORMANCE</div>
<div class="label" style="left:697px; top:628px;">BUILDS CONFIDENCE</div>
<div class="label" style="left:671px; top:679px;">CHANGES AWARENESS</div>

</body>
</html>
```